Custom Label for Women's Supplement Brand

Need a product label for our products, we have a logo designed but need to incorporate it in to our product line which will have capsule bottles, tincture bottles, and eventually skin care. We originally wanted a label that had black as main color, but are open to options. Want it to be sleek, and pull the eye, simple yet fun. Even something different that doesn’t look like anyone else.
Updates

Low designer entries

Target Market(s)

Women 26-70

Requirements
Nice to have
• Would love some metallic accents

```html
<!DOCTYPE html>
<html lang="en">
<head>
<meta charset="utf-8">
<title>Multi Vitamine for Women – Label</title>
<link rel="stylesheet" href="https://fonts.googleapis.com/css2?family=Lexend:wght@600&family=Fredoka:wght@500&family=Montserrat:wght@400;500&display=swap">
<style>
  :root {
    --page: #ffffff;
    --label-black: #161616;
    --band-orange: #f0a13c;
    --lime: #8cbd2e;
    --soft-grey: #c9c9c9;
    --badge-blue: #1aa6cf;
    --white: #ffffff;
    --placeholder-light: #9a9a9a;
    --placeholder-dark: #5e5e5e;
  }
  * { margin: 0; padding: 0; box-sizing: border-box; }
  html, body {
    width: 1193px;
    height: 1200px;
    overflow: hidden;
    background: var(--page);
  }
  .label {
    position: absolute;
    left: 304px;
    top: 233px;
    width: 584px;
    height: 733px;
    background: var(--label-black);
    overflow: hidden;
  }
  .side-band {
    position: absolute;
    left: 0;
    top: 0;
    width: 88px;
    height: 560px;
  }
  .side-band-word {
    position: absolute;
    left: 44px;
    top: 392px;
    transform: translate(-50%, -50%) rotate(-90deg);
    font-family: "Lexend", sans-serif;
    font-weight: 600;
    font-size: 66px;
    line-height: 1;
    color: var(--label-black);
    white-space: nowrap;
  }
  .brand {
    position: absolute;
    left: 97px;
    width: 300px;
    top: 77px;
    text-align: center;
  }
  .brand-dot {
    display: block;
    width: 56px;
    height: 56px;
    margin: 0 auto 14px;
    border-radius: 50%;
    background: var(--lime);
  }
  .brand-name {
    font-family: "Fredoka", sans-serif;
    font-weight: 500;
    font-size: 34px;
    line-height: 1;
    color: var(--lime);
    white-space: nowrap;
  }
  .brand-tagline {
    display: flex;
    align-items: center;
    justify-content: center;
    gap: 10px;
    margin-top: 8px;
    font-family: "Fredoka", sans-serif;
    font-weight: 500;
    font-size: 15px;
    letter-spacing: 4px;
    color: var(--lime);
  }
  .brand-tagline::before,
  .brand-tagline::after {
    content: "";
    width: 66px;
    height: 2px;
    background: var(--lime);
  }
  .product-name {
    position: absolute;
    left: 108px;
    top: 272px;
    font-family: "Lexend", sans-serif;
    font-weight: 600;
    font-size: 104px;
    line-height: 0.88;
    letter-spacing: -1px;
    color: var(--lime);
  }
  .product-audience {
    position: absolute;
    left: 108px;
    top: 478px;
    font-family: "Montserrat", sans-serif;
    font-weight: 400;
    font-size: 33px;
    letter-spacing: 4px;
    color: var(--soft-grey);
    white-space: nowrap;
  }
  .accent-placeholder {
    position: absolute;
    left: 6px;
    top: 549px;
    width: 178px;
    height: 128px;
    background: linear-gradient(135deg, var(--placeholder-light), var(--placeholder-dark));
  }
  .count-badge {
    position: absolute;
    left: 349px;
    top: 586px;
    width: 94px;
    height: 83px;
    border-radius: 12px;
    background: var(--badge-blue);
    color: var(--white);
    text-align: center;
    padding-top: 12px;
  }
  .count-number {
    display: block;
    font-family: "Montserrat", sans-serif;
    font-weight: 500;
    font-size: 36px;
    line-height: 1;
  }
  .count-unit {
    display: block;
    font-family: "Montserrat", sans-serif;
    font-size: 13px;
    margin-top: 5px;
  }
</style>
</head>
<body>
  <main class="label">
    <svg class="side-band" viewBox="0 0 88 560" aria-hidden="true">
      <polygon points="0,0 88,0 88,517 0,560" fill="var(--band-orange)"/>
    </svg>
    <div class="side-band-word">Multi</div>

    <header class="brand">
      <span class="brand-dot"></span>
      <div class="brand-name">Sunny Centered</div>
      <div class="brand-tagline">WELLNESS</div>
    </header>

    <h1 class="product-name">Vita<br>mine</h1>
    <p class="product-audience">for women</p>

    <div class="accent-placeholder" role="img" aria-label="Metallic silver leaf accent"></div>

    <div class="count-badge">
      <span class="count-number">30</span>
      <span class="count-unit">Capsules</span>
    </div>
  </main>
</body>
</html>
```